Building company requiring web site design

We need a web design for a new company based in Sydney called Marlow Building Co. We build and renovate new and existing homes for consumers. We would like to see design that use the colours red and grey. The final design should communicate innovative building but with old fashion quality, great customer service and attention to detail. I have already had a logo and stationary design completed and would like to use the these colour schemes
Updates

Target Market(s)

Home owners, investors

Industry/Entity Type

Building

Coding

Coded - Design and coding required

Number of Pages Required

5+ page

Requirements
Must have
• Home page, contact page, about us page, gallery page and testimonial page
Nice to have
• Contact form

```html
<!DOCTYPE html>
<html lang="en">
<head>
<meta charset="utf-8">
<title>Marlow Building Co.</title>
<link href="https://fonts.googleapis.com/css2?family=Antonio:wght@300;400;600&family=Open+Sans:wght@400;600;700&display=swap" rel="stylesheet">
<style>
:root{
  --red:#b34444;
  --red-nav:#c0392b;
  --dark:#2e2e2e;
  --ink:#333333;
  --text:#555555;
  --muted:#777777;
  --line:#bbbbbb;
  --button:#6e6e6e;
  --white:#ffffff;
}
*{margin:0;padding:0;box-sizing:border-box}
html,body{width:709px;height:1200px;overflow:hidden;background:var(--white)}
body{position:relative;font-family:"Open Sans",sans-serif;color:var(--text)}
.abs{position:absolute}
.heading{font-family:"Antonio",sans-serif}

/* header */
.site-header{left:0;top:0;width:709px;height:64px;background:var(--white)}
.brand{left:46px;top:18px;display:flex;align-items:center;gap:6px}
.brand-mark{width:14px;height:14px;background:var(--red)}
.brand-name{font-family:"Open Sans",sans-serif;font-weight:700;font-size:13px;color:var(--ink)}
.main-nav{top:43px;font-size:8.5px;font-weight:600;color:var(--ink);letter-spacing:.2px}
.main-nav a{position:absolute;white-space:nowrap;color:inherit;text-decoration:none}
.main-nav a.active{color:var(--red-nav)}

/* hero */
.hero{left:0;top:65px;width:709px;height:396px;background:linear-gradient(180deg,#6d8cb1 0%,#3f4f56 35%,#7a5a3a 60%,#5d5550 85%,#4a4a48 100%)}
.hero-title{left:0;top:356px;width:709px;text-align:center;color:var(--white);font-family:"Antonio",sans-serif;font-weight:600;font-size:29px;line-height:34px;letter-spacing:.2px}
.hero-sub{left:0;top:391px;width:709px;text-align:center;color:var(--white);font-family:"Antonio",sans-serif;font-weight:600;font-size:17px;line-height:20px}

/* intro */
.intro-title{left:0;top:488px;width:709px;text-align:center;font-weight:300;font-size:22px;color:var(--ink)}
.intro-text{left:104px;top:520px;width:501px;text-align:center;font-size:10px;line-height:16.5px;color:var(--text)}
.outline-btn{left:310px;top:584px;width:90px;height:19px;border:1px solid var(--ink);font-size:8px;line-height:17px;text-align:center;color:var(--ink)}

/* testimonial */
.testimonial{left:0;top:636px;width:709px;height:152px;background:var(--dark)}
.quote{left:140px;top:670px;width:429px;text-align:center;font-size:7.3px;line-height:13.5px;color:#dddddd}
.avatar{left:333px;top:706px;width:46px;height:46px;border-radius:50%;background:linear-gradient(180deg,#cfd2d4,#9a8f88);border:2px solid #eeeeee}
.client{left:0;top:755px;width:709px;text-align:center;font-size:7px;color:#cccccc}

/* project + contact */
.section-title{font-weight:300;font-size:21px;color:var(--ink);line-height:24px}
.title-rule{width:37px;height:3px;background:var(--dark)}
.project-photo{left:44px;top:856px;width:302px;height:158px;background:linear-gradient(180deg,#e9edf0 0%,#a9adb0 45%,#6f7268 75%,#9a9c98 100%)}
.project-name{left:363px;top:863px;font-size:9.5px;font-weight:700;color:var(--ink)}
.project-place{left:363px;top:876px;font-size:7px;color:var(--ink)}
.project-desc{left:363px;top:903px;width:132px;font-size:7.3px;line-height:13.2px;color:var(--text)}
.solid-btn{height:18px;background:var(--button);color:var(--white);font-size:6.5px;font-weight:700;line-height:18px;text-align:center}
.divider{width:1px;background:var(--line)}
.form-lead{left:522px;top:862px;font-size:10px;font-weight:700;color:var(--ink)}
.form-note{left:522px;top:876px;font-size:7px;color:var(--ink)}
.field{left:522px;width:107px;height:17px;border:1px solid var(--line);font-size:6.5px;font-style:italic;color:#aaaaaa;padding-left:6px;line-height:15px}

/* footer */
.site-footer{left:0;top:1064px;width:709px;height:136px;background:var(--red)}
.footer-title{left:45px;top:1090px;font-size:13px;font-weight:300;color:var(--dark)}
.thumb{top:1118px;width:56px;height:44px;background:linear-gradient(180deg,#9fb3c6 0%,#6d7a80 55%,#5f8a4d 100%)}
.thumb.alt{background:linear-gradient(180deg,#d8c9a8 0%,#8c6b4a 55%,#6a7a4d 100%)}
.phone{left:374px;top:1098px;font-family:"Antonio",sans-serif;font-weight:300;font-size:17px;color:var(--dark)}
.contact-line{left:376px;font-size:7.3px;line-height:9.5px;color:var(--dark)}
.social{top:1104px;width:12px;height:12px;border-radius:50%;background:var(--dark)}
.copyright{left:523px;top:1132px;font-size:7.3px;line-height:10px;color:var(--dark)}
</style>
</head>
<body>

<header class="abs site-header">
  <div class="abs brand"><span class="brand-mark"></span><span class="brand-name">Marlow Building Co.</span></div>
  <nav class="abs main-nav">
    <a class="active" style="left:333px">HOME</a>
    <a style="left:382px">ABOUT US</a>
    <a style="left:449px">GALLERY</a>
    <a style="left:510px">TESTIMONIALS</a>
    <a style="left:596px">CONTACT US</a>
  </nav>
</header>

<section class="abs hero" role="img" aria-label="Photograph of a modern gabled timber home lit up at dusk"></section>
<h1 class="abs hero-title">STATE OF THE ART DESIGN / OLD WORLD CRAFTMANSHIP</h1>
<p class="abs hero-sub">BUILDING REPAIRS - RENOVATIONS - CONSTRUCTION MANAGEMENT</p>

<h2 class="abs heading intro-title">Hello.</h2>
<p class="abs intro-text">We are a new company based in Sydney called Marlow Building Co. We build and renovate new and existing homes for our clients. Our speciality is innovative building but with old fashion quality, great customer service &amp; attention to detail.</p>
<div class="abs outline-btn">KNOW MORE</div>

<section class="abs testimonial"></section>
<svg class="abs" style="left:44px;top:698px" width="14" height="26" viewBox="0 0 14 26"><path d="M12 1 L2 13 L12 25" fill="none" stroke="#666" stroke-width="2"/></svg>
<svg class="abs" style="left:650px;top:698px" width="14" height="26" viewBox="0 0 14 26"><path d="M2 1 L12 13 L2 25" fill="none" stroke="#666" stroke-width="2"/></svg>
<p class="abs quote">We are glad that we chose Marlow Builders &amp; are really pleased with our new home. They had our house completed ahead of schedule and did not compromise on quality. Sincerely recommend them..</p>
<div class="abs avatar" role="img" aria-label="Client portrait"></div>
<p class="abs client">Sam Whitfield</p>

<h2 class="abs heading section-title" style="left:44px;top:814px">LATEST PROJECT</h2>
<div class="abs title-rule" style="left:44px;top:842px"></div>
<div class="abs project-photo" role="img" aria-label="Photograph of a curved modern art gallery building"></div>
<h3 class="abs project-name">NORTHLIGHT ART GALLERY</h3>
<p class="abs project-place">New York, USA</p>
<p class="abs project-desc">Efficiently unleash cross-media information without cross-media value. Quickly maximize timely deliverables for real-time schemas. Dramatically maintain solutions without functional solutions.</p>
<div class="abs solid-btn" style="left:362px;top:996px;width:90px">VIEW MORE PROJECTS</div>

<div class="abs divider" style="left:505px;top:816px;height:198px"></div>

<h2 class="abs heading section-title" style="left:522px;top:814px">NEED MORE INFO?</h2>
<div class="abs title-rule" style="left:522px;top:842px"></div>
<p class="abs form-lead">Just drop us a line..</p>
<p class="abs form-note">We'll get back to you.</p>
<div class="abs field" style="top:903px">Your Name</div>
<div class="abs field" style="top:930px">Your Email</div>
<div class="abs field" style="top:958px">Your Phone #</div>
<div class="abs solid-btn" style="left:522px;top:996px;width:68px">SEND MAIL</div>

<footer class="abs site-footer"></footer>
<h2 class="abs heading footer-title">RECENT PROJECTS</h2>
<svg class="abs" style="left:42px;top:1133px" width="8" height="14" viewBox="0 0 8 14"><path d="M7 1 L2 7 L7 13" fill="none" stroke="#e27a7a" stroke-width="2"/></svg>
<div class="abs thumb" role="img" aria-label="Apartment project photo" style="left:53px"></div>
<div class="abs thumb alt" role="img" aria-label="Heritage home project photo" style="left:110px"></div>
<div class="abs thumb" role="img" aria-label="Apartment project photo" style="left:167px"></div>
<div class="abs thumb alt" role="img" aria-label="Heritage home project photo" style="left:224px"></div>
<div class="abs thumb" role="img" aria-label="Apartment project photo" style="left:281px"></div>
<svg class="abs" style="left:339px;top:1133px" width="8" height="14" viewBox="0 0 8 14"><path d="M1 1 L6 7 L1 13" fill="none" stroke="#e27a7a" stroke-width="2"/></svg>

<svg class="abs" style="left:362px;top:1101px" width="9" height="14" viewBox="0 0 9 14"><path d="M2 1 h3 l1 3 -2 1 q0 3 2 5 l2 -1 1 3 -2 1 q-6 -4 -5 -12z" fill="#e27a7a"/></svg>
<p class="abs phone">(03) 5550 2417</p>
<svg class="abs" style="left:363px;top:1128px" width="9" height="7" viewBox="0 0 9 7"><rect x=".5" y=".5" width="8" height="6" fill="none" stroke="#e27a7a"/><path d="M.5 .5 L4.5 4 L8.5 .5" fill="none" stroke="#e27a7a"/></svg>
<p class="abs contact-line" style="top:1127px">info@marlowbuilders.com.au</p>
<svg class="abs" style="left:363px;top:1146px" width="8" height="11" viewBox="0 0 8 11"><path d="M4 10 L1 5 A3.2 3.2 0 1 1 7 5 Z" fill="none" stroke="#e27a7a" stroke-width="1.2"/><circle cx="4" cy="3.8" r="1.1" fill="#e27a7a"/></svg>
<p class="abs contact-line" style="top:1146px">18 Elmwood Lane, Melbourne,<br>Victoria 3004</p>

<div class="abs divider" style="left:506px;top:1098px;height:68px;background:var(--dark)"></div>
<div class="abs social" style="left:523px" aria-label="Social link"></div>
<div class="abs social" style="left:541px" aria-label="Social link"></div>
<div class="abs social" style="left:559px" aria-label="Social link"></div>
<div class="abs social" style="left:577px" aria-label="Social link"></div>
<p class="abs copyright">© MARLOW Building Co.<br>2016 All Rights Reserved</p>

</body>
</html>
```